Tallbrook Meridian Advisory needs business cards

Tallbrook Meridian Advisory is a new approach to consulting: we believe in partnering our clients in a hands-on, side-by-side, rolling-up-our sleeves approach, rather than being removed and aloof consultants.

We have a logo design developped through PixelHarbor (see attachment) and need to move to the stage of designing a business card for our 7 founding members.

Target Market(s)

Senior executives in local and global companies (such as Fizzmont Tonic, Hollanby, Brevard, etc)

Industry/Entity Type

Business

Requirements
Must have
• Look and feel: The design reflect the logo: i.e. professional, modern and approachable (as opposed to corporate traditional and remote). We are looking for a high quality, premium design.

Content must haves:
- prominent: our logo, person's name, function, phone number and e-mail address
- less prominent: company address and website

Example: Tallbrook Meridian Advisory logo, Mireille Vostag, Partner, +44 (0)781 209 3375, mireille_vostag@tallbrookmeridian.example / 17 Pelham Crescent, Esher, Surrey, UK, KT10 3WN - www.tallbrookmeridian.example

- Both sides of the card can be used
- Both versions of the logo can be used (on black or on white)

```html
<!DOCTYPE html>
<html lang="en">
<head>
<meta charset="utf-8">
<title>Tallbrook Meridian Advisory – Business Cards</title>
<link href="https://fonts.googleapis.com/css2?family=Open+Sans:wght@400;600;700&display=swap" rel="stylesheet">
<style>
  :root {
    --stage: #ece9e4;
    --card-white: #ffffff;
    --ink: #1d1d1f;
    --text-grey: #4a4a4a;
    --divider: #b5b5b5;
    --brand-blue: #1b9ad8;
    --brand-blue-light: #7fd0f2;
    --brand-blue-deep: #0a74b8;
    --swoosh: #1a1a1a;
    --grey-light: #9a9a9c;
    --grey-dark: #4c4c4e;
    --on-dark: #f2f2f2;
  }
  * { box-sizing: border-box; margin: 0; padding: 0; }
  html, body { width: 1200px; height: 393px; overflow: hidden; }
  body {
    background: var(--stage);
    font-family: "Open Sans", Arial, sans-serif;
    position: relative;
  }
  .card {
    position: absolute;
    width: 515px;
    height: 294px;
    border-radius: 16px;
    overflow: hidden;
    box-shadow: 0 2px 6px rgba(0,0,0,.25);
  }
  .card--front { left: 61px; top: 51px; background: var(--card-white); }
  .card--back {
    left: 609px; top: 46px;
    background: radial-gradient(ellipse at 38% 35%, var(--grey-light) 0%, #737375 50%, var(--grey-dark) 100%);
  }

  .brand { position: absolute; display: flex; align-items: center; }
  .brand__dot { border-radius: 50%; background: var(--brand-blue); flex: none; }
  .brand__name {
    font-weight: 700;
    line-height: 1.02;
    letter-spacing: -0.5px;
  }
  .card--front .brand { left: 109px; top: 29px; }
  .card--front .brand__dot { width: 96px; height: 96px; }
  .card--front .brand__name { color: var(--ink); font-size: 25px; margin-left: 22px; }
  .card--back .brand { left: 93px; top: 75px; }
  .card--back .brand__dot { width: 120px; height: 120px; }
  .card--back .brand__name { color: var(--on-dark); font-size: 28px; margin-left: 14px; }

  .address {
    position: absolute;
    right: 297px; top: 151px;
    text-align: right;
    font-size: 12px;
    line-height: 21px;
    color: var(--text-grey);
  }
  .divider {
    position: absolute;
    left: 230px; top: 154px;
    width: 1px; height: 60px;
    background: var(--divider);
  }
  .contacts {
    position: absolute;
    left: 241px; top: 151px;
    list-style: none;
    font-size: 12px;
    line-height: 21px;
    color: var(--text-grey);
  }
  .contacts li { display: flex; align-items: center; }
  .contacts svg { width: 10px; height: 10px; margin-right: 7px; fill: var(--text-grey); flex: none; }

  .wave { position: absolute; left: 0; bottom: 0; width: 515px; height: 90px; }
  .holder {
    position: absolute;
    left: 45px; bottom: 12px;
    color: #fff;
    font-size: 14.5px;
    font-weight: 700;
  }
  .holder__role { font-weight: 400; font-size: 12.5px; }

  .website {
    position: absolute;
    left: 0; right: 0; top: 227px;
    text-align: center;
    color: var(--on-dark);
    font-size: 12px;
    letter-spacing: 1.4px;
  }
</style>
</head>
<body>

<section class="card card--front" aria-label="Business card front">
  <div class="brand">
    <span class="brand__dot"></span>
    <span class="brand__name">Tallbrook Meridian<br>Advisory</span>
  </div>

  <address class="address" style="font-style:normal">
    17 Pelham Crescent, Esher<br>Surrey, UK, KT10 3WN
  </address>
  <span class="divider"></span>
  <ul class="contacts">
    <li><svg viewBox="0 0 10 10"><path d="M2 0.5l2 2-1 1.2c.6 1.3 1.6 2.3 2.9 2.9l1.2-1 2 2-1.3 1.6C4.6 9 1 5.4.4 1.8z"/></svg>+44 (0)781 209 3375</li>
    <li><svg viewBox="0 0 10 10"><path d="M0 2h10v6H0z M0 2l5 3.5L10 2" stroke="#fff" stroke-width=".8"/></svg>mireille_vostag@tallbrookmeridian.example</li>
    <li><svg viewBox="0 0 10 10"><circle cx="5" cy="5" r="4.5"/></svg>www.tallbrookmeridian.example</li>
  </ul>

  <svg class="wave" viewBox="0 0 515 90" preserveAspectRatio="none" aria-hidden="true">
    <defs>
      <linearGradient id="bandBlue" x1="0" y1="0" x2="1" y2="0">
        <stop offset="0" stop-color="var(--brand-blue-deep)"/>
        <stop offset=".45" stop-color="var(--brand-blue-light)"/>
        <stop offset="1" stop-color="var(--brand-blue)"/>
      </linearGradient>
    </defs>
    <path d="M0 14 C120 4 230 30 320 52 C400 70 470 58 515 44 L515 54 C460 74 390 80 310 64 C220 44 120 22 0 30 Z" fill="var(--swoosh)"/>
    <path d="M0 30 C120 22 220 44 310 64 C390 80 460 74 515 54 L515 90 L0 90 Z" fill="url(#bandBlue)"/>
  </svg>
  <p class="holder">Mireille Vostag , <span class="holder__role">Partner</span></p>
</section>

<section class="card card--back" aria-label="Business card back">
  <div class="brand">
    <span class="brand__dot"></span>
    <span class="brand__name">Tallbrook Meridian<br>Advisory</span>
  </div>
  <p class="website">www.tallbrookmeridian.example</p>
</section>

</body>
</html>
```